Brightwave Gherkins, we sell different color pickles that are different flavors

I need nice packaging done for my product, I sell different color pickles.
1. Uploaded photo of my logo, packaging inspiration, also the nutrition facts I want on the packaging as well.
2. This is the stuff I want on my packaging. Packaging, Refrigerator after opening
Packaging, Fresh packaging
Packaging, liquid inside, be careful while opening
Packaging, resealable
Packaging, social media, instragram: @brightwavegherkins and Facebook: @brightwavegherkins
Packaging, sku

Product description:
Looking for a delicious and refreshing snack? Look no further than Brightwave Gherkins! Our pickles are crunchy and full of flavor, and they make a great addition to any meal. We offer a variety of flavors, so there's something for everyone to enjoy. Be sure to check us out today! You won't be disappointed!

Nutrition label on back of packaging, uploaded it

Target Market(s)

Pickle lovers, kids

Font styles to use
Decorative

Colors

Designer to choose colors to be used in the design.

Requirements
Must have
• Bright colors, friendly looking, eye catching
Nice to have
• My social media on my packaging, the flavor, the fruit of the flavor on the package with water on it
Should not have
• Dark colors

```html
<!DOCTYPE html>
<html lang="en">
<head>
<meta charset="UTF-8">
<title>Brightwave Gherkins – Lemonade Crunchy Pickles Pouch</title>
<link href="https://fonts.googleapis.com/css2?family=Bangers&family=Poppins:wght@600&display=swap" rel="stylesheet">
<style>
  :root {
    --page-bg: #ffffff;
    --pouch-cream: #f7ece6;
    --pouch-cream-edge: #efdcd1;
    --ray-peach: #f3cfae;
    --lemon-yellow: #f3bd1c;
    --lemon-deep: #e9a90e;
    --title-yellow: #f1bf17;
    --ink-black: #1d1d1d;
    --accent-orange: #e46a1f;
    --ribbon-white: #fbf7f3;
    --badge-white: #ffffff;
    --zip-line: #e6d2c6;
  }
  * { box-sizing: border-box; margin: 0; padding: 0; }
  html, body {
    width: 1200px;
    height: 900px;
    overflow: hidden;
    background: var(--page-bg);
  }
  .canvas {
    position: relative;
    width: 1200px;
    height: 900px;
  }
  .pouch {
    position: absolute;
    left: 340px;
    top: 40px;
    width: 520px;
    height: 820px;
    border-radius: 14px 14px 26px 26px;
    background:
      radial-gradient(ellipse at 50% 38%, var(--pouch-cream) 0%, var(--pouch-cream) 45%, var(--ray-peach) 140%);
    overflow: hidden;
    box-shadow: inset 0 0 0 2px var(--pouch-cream-edge);
  }
  .pouch__seal {
    position: absolute;
    left: 0; right: 0; top: 0;
    height: 70px;
    background: var(--pouch-cream-edge);
    opacity: .55;
  }
  .pouch__zip {
    position: absolute;
    left: 0; right: 0; top: 118px;
    height: 3px;
    background: var(--zip-line);
  }
  .brand {
    position: absolute;
    top: 170px;
    left: 0; right: 0;
    text-align: center;
  }
  .brand__name {
    display: inline-flex;
    align-items: center;
    gap: 10px;
    font-family: 'Bangers', cursive;
    font-size: 54px;
    letter-spacing: 2px;
    color: var(--accent-orange);
    line-height: 1;
  }
  .brand__mark {
    width: 22px; height: 22px;
    border-radius: 50%;
    background: var(--accent-orange);
  }
  .brand__tagline {
    margin-top: 6px;
    font-family: 'Bangers', cursive;
    font-size: 20px;
    letter-spacing: 1.5px;
    color: var(--ink-black);
  }
  .flavor {
    position: absolute;
    top: 290px;
    left: 0; right: 0;
    text-align: center;
    transform: rotate(-4deg);
  }
  .flavor__name {
    font-family: 'Bangers', cursive;
    font-size: 92px;
    letter-spacing: 3px;
    color: var(--title-yellow);
    line-height: 1;
  }
  .flavor__product {
    font-family: 'Bangers', cursive;
    font-size: 48px;
    letter-spacing: 2px;
    color: var(--ink-black);
    line-height: 1.05;
  }
  .band {
    position: absolute;
    left: 0; right: 0; bottom: 0;
    height: 400px;
    background: linear-gradient(180deg, var(--lemon-yellow), var(--lemon-deep));
    clip-path: polygon(0 22%, 100% 0, 100% 100%, 0 100%);
  }
  .lemon-art {
    position: absolute;
    left: 60px;
    top: 460px;
    width: 330px;
    height: 300px;
    border-radius: 50%;
    background: radial-gradient(circle at 48% 48%, #fff4a8 0%, #f8e04a 45%, #f0c21a 75%, rgba(240,194,26,0) 100%);
  }
  .badge {
    position: absolute;
    right: 48px;
    top: 470px;
    width: 104px; height: 104px;
    border-radius: 50%;
    background: var(--badge-white);
    border: 3px solid var(--lemon-yellow);
    display: flex;
    flex-direction: column;
    align-items: center;
    justify-content: center;
    font-family: 'Bangers', cursive;
    font-size: 20px;
    letter-spacing: 1px;
    line-height: 1.05;
    color: var(--accent-orange);
    transform: rotate(-8deg);
  }
  .ribbon {
    position: absolute;
    left: -20px;
    right: -20px;
    bottom: 42px;
    height: 50px;
    background: var(--ribbon-white);
    transform: rotate(-8deg);
    display: flex;
    align-items: center;
    justify-content: center;
    font-family: 'Poppins', sans-serif;
    font-weight: 600;
    font-size: 22px;
    letter-spacing: 7px;
    color: var(--accent-orange);
  }
</style>
</head>
<body>
  <main class="canvas">
    <section class="pouch" aria-label="Lemonade crunchy pickles pouch front">
      <div class="pouch__seal"></div>
      <div class="pouch__zip"></div>

      <header class="brand">
        <div class="brand__name"><span class="brand__mark"></span>Brightwave Gherkins</div>
        <p class="brand__tagline">Game Changing Flavor</p>
      </header>

      <div class="flavor">
        <h1 class="flavor__name">Lemonade</h1>
        <h2 class="flavor__product">Crunchy Pickles</h2>
      </div>

      <div class="band"></div>
      <div class="lemon-art" role="img" aria-label="Halved lemon with leaves and a splash of lemonade juice"></div>

      <div class="badge"><span>Fresh</span><span>Packaging</span></div>

      <div class="ribbon">VARIETY OF FLAVORS</div>
    </section>
  </main>
</body>
</html>
```